Oven Cleaning Business owner needs business card design

Hi there,
Would like for a business card to be designed for myself, the owner of a professional oven cleaning business on the Sunshine Coast.
Would like it to look sleek, and modern-ish. Bit creative is encouraged too.
Include following:
Name/title: Corin ter Haghe, Owner
Phone number: 1300 482 916
Email: info@hearthshinecrew.com.au
Website: www.hearthshinecrew.com.au

```html
<!DOCTYPE html>
<html lang="en">
<head>
<meta charset="utf-8">
<title>Hearthshine Crew – Business Card</title>
<link rel="stylesheet" href="https://fonts.googleapis.com/css2?family=Lato:wght@400;700;900&display=swap">
<style>
  :root {
    --teal: #52c3cb;
    --ink: #111111;
    --card: #ffffff;
    --backdrop: #d9dadc;
    --text: #222222;
  }
  * { margin: 0; padding: 0; box-sizing: border-box; }
  html, body { width: 1200px; height: 900px; overflow: hidden; }
  body {
    background: var(--backdrop);
    font-family: "Lato", sans-serif;
    color: var(--text);
    position: relative;
  }
  .card {
    position: absolute;
    left: 280px;
    width: 640px;
    height: 366px;
    background: var(--card);
    border-radius: 36px;
    box-shadow: 0 6px 18px rgba(0,0,0,0.18);
    overflow: hidden;
  }
  .card--front { top: 60px; }
  .card--back { top: 474px; }

  .brand {
    display: flex;
    align-items: center;
    gap: 14px;
  }
  .brand__dot {
    width: 22px; height: 22px;
    border-radius: 50%;
    background: var(--teal);
    flex: none;
  }
  .brand__name {
    font-weight: 900;
    color: var(--ink);
    letter-spacing: 0.02em;
    white-space: nowrap;
  }

  .card--front .brand {
    position: absolute;
    left: 0; right: 0; top: 0; bottom: 0;
    justify-content: center;
  }
  .card--front .brand__name { font-size: 50px; }
  .card--front .brand__dot { width: 34px; height: 34px; }

  .card--back .brand {
    position: absolute;
    left: 40px; top: 52px;
  }
  .card--back .brand__name { font-size: 32px; }

  .back__mark {
    position: absolute;
    right: 40px; top: 44px;
    width: 210px; height: 210px;
    border-radius: 50%;
    background: var(--teal);
  }

  .person {
    position: absolute;
    left: 40px; top: 160px;
    padding-left: 22px;
    border-left: 12px solid var(--teal);
  }
  .person__name {
    font-size: 30px;
    font-weight: 400;
    color: var(--teal);
    line-height: 1.1;
  }
  .person__title {
    font-size: 15px;
    color: var(--text);
    margin-top: 4px;
  }

  .contact {
    position: absolute;
    left: 74px; top: 262px;
    list-style: none;
  }
  .contact__item {
    display: flex;
    align-items: center;
    gap: 10px;
    font-size: 15px;
    line-height: 26px;
  }
  .contact__icon {
    width: 15px; height: 15px;
    fill: var(--teal);
    flex: none;
  }
</style>
</head>
<body>

  <section class="card card--front">
    <div class="brand">
      <span class="brand__dot"></span>
      <span class="brand__name">Hearthshine Crew</span>
    </div>
  </section>

  <section class="card card--back">
    <div class="brand">
      <span class="brand__name">Hearthshine Crew</span>
    </div>

    <div class="back__mark"></div>

    <div class="person">
      <p class="person__name">Corin ter Haghe</p>
      <p class="person__title">Owner</p>
    </div>

    <ul class="contact">
      <li class="contact__item">
        <svg class="contact__icon" viewBox="0 0 16 16" aria-hidden="true">
          <path d="M3.5 1.5l2.5 0 1 3.5-1.7 1.2a8 8 0 0 0 4.5 4.5l1.2-1.7 3.5 1v2.5c0 .8-.7 1.5-1.5 1.5A12 12 0 0 1 2 3c0-.8.7-1.5 1.5-1.5z"/>
        </svg>
        <span>1300 482 916</span>
      </li>
      <li class="contact__item">
        <svg class="contact__icon" viewBox="0 0 16 16" aria-hidden="true">
          <path d="M1 3h14v10H1z M1.5 3.5L8 9l6.5-5.5" fill="var(--teal)" stroke="#fff" stroke-width="1"/>
        </svg>
        <span>info@hearthshinecrew.com.au</span>
      </li>
      <li class="contact__item">
        <svg class="contact__icon" viewBox="0 0 16 16" aria-hidden="true">
          <circle cx="8" cy="8" r="7"/>
          <path d="M1 8h14M8 1c-3 3.5-3 10.5 0 14M8 1c3 3.5 3 10.5 0 14" fill="none" stroke="#fff" stroke-width="1"/>
        </svg>
        <span>www.hearthshinecrew.com.au</span>
      </li>
    </ul>
  </section>

</body>
</html>
```